Event Graphics Needed for a Youth Camp

I need graphics designed for our summer camps event. These camps are for teenagers, 6-12th grades. The design visual appeal should be geared to older teenagers.
Primary graphic design is for a 11x17 poster.
Graphic should include the following:
-Please include cut and bleed lines.
-Main Title: KV Rootline presents . . . Summer Camp
-Dates: Teen Camp - June 5-9; High School Camp - June 19-23; Middle School Camp - June 26-30.
-Register at RivoTrailWeek.com
-Tamsin Brook Retreat Center, Deadwood, SD
-For each camp, include name and headshot of speaker: Teen: Luka Brevant, High School: Timo Wexley, Middle School: Colin Marbury.
-Include KV Rootline logo
I will also need the images redesigned for:
-a social media graphic
-Include KV Rootline logo
-16x9 title slide
-Include KV Rootline logo
- a postcard sized 3.5 X 5 inches
-(If possible) For each camp, include name and headshot of speaker: Teen: Luka Brevant, High School: Timo Wexley, Middle School: Colin Marbury.
-Include KV Rootline logo
-Event Graphic should be attractive to older teenagers. Open to ideas. I want a bright not dark design. Do not include palm trees. Our location is in a pine tree forest in the Black Hills of South Dakota.
My graphic design experience is limited. I will need help receiving the files I need in the various sizes. Thank you.

```html
<!DOCTYPE html>
<html lang="en">
<head>
<meta charset="utf-8">
<title>KV Rootline Summer Camp 2023</title>
<link href="https://fonts.googleapis.com/css2?family=Barlow+Condensed:wght@600;700&family=Fredoka:wdth,wght@75..125,700&family=Oswald:wght@300&display=swap" rel="stylesheet">
<style>
:root{
  --stage:#c8e1e6;
  --forest:#1b3b34;
  --cream:#e6c98f;
  --gold:#f2b22a;
  --amber:#e9a424;
  --coral:#ee4a25;
  --sage:#4f7a5e;
  --pine-panel:#176b3b;
  --sand:#e9d8ad;
  --ink:#1b3b34;
  --white:#ffffff;
  --photo-a:#8a8a8a;
  --photo-b:#3a3a3a;
}
*{box-sizing:border-box;margin:0;padding:0}
html,body{width:1200px;height:968px;overflow:hidden;background:var(--stage)}
.canvas{position:relative;width:1200px;height:968px}
.piece{position:absolute;background:var(--forest);overflow:hidden}
.poster{left:42px;top:63px;width:545px;height:841px}
.social{left:622px;top:60px;width:533px;height:533px}
.slide{left:627px;top:606px;width:523px;height:294px}
.abs{position:absolute}
.presents{font-family:"Oswald",sans-serif;font-weight:300;color:var(--cream);letter-spacing:.5px;white-space:nowrap;text-transform:uppercase}
.title{font-family:"Fredoka",sans-serif;font-weight:700;font-stretch:80%;color:var(--cream);line-height:1;white-space:nowrap;transform:rotate(-2deg);transform-origin:left bottom;letter-spacing:-1px}
.camp-lockup{display:flex;align-items:baseline;white-space:nowrap;transform:rotate(-2deg);transform-origin:left bottom;line-height:1}
.camp-word{font-family:"Fredoka",sans-serif;font-weight:700;font-stretch:80%;color:var(--cream);letter-spacing:-1px}
.year{font-family:"Fredoka",sans-serif;font-weight:700;font-stretch:80%;color:var(--gold)}
.panel{background:var(--pine-panel)}
.scene{background:var(--sage)}
.sun{border-radius:50%;background:var(--coral)}
.badge{border-radius:50%;background:var(--white);display:flex;align-items:center;justify-content:center;text-align:center}
.badge-name{font-family:"Barlow Condensed",sans-serif;font-weight:700;color:var(--ink);line-height:1}
.cond{font-family:"Barlow Condensed",sans-serif;font-weight:700;color:var(--cream);text-transform:uppercase;white-space:nowrap;line-height:1.15}
.date{display:flex;align-items:center;gap:4px;color:var(--white)}
.date svg{flex:none}
.cta{background:var(--amber);color:var(--ink);display:flex;align-items:center;justify-content:center;font-family:"Barlow Condensed",sans-serif;font-weight:700;text-transform:uppercase;white-space:nowrap}
.speaker-card{overflow:hidden}
.speaker-card.teen{background:var(--coral)}
.speaker-card.high{background:var(--sand)}
.speaker-card.middle{background:var(--sage)}
.speaker-tag{position:absolute;left:6px;font-family:"Barlow Condensed",sans-serif;font-weight:700;font-size:8px;text-transform:uppercase;letter-spacing:.3px}
.speaker-name{position:absolute;left:6px;font-family:"Barlow Condensed",sans-serif;font-weight:700;font-size:13px;line-height:1.3;text-transform:uppercase}
.teen .speaker-tag{color:var(--sand);top:14px}.teen .speaker-name{color:var(--white);top:26px}
.high .speaker-tag{color:var(--sage);top:20px}.high .speaker-name{color:var(--sage);top:32px}
.middle .speaker-tag{color:var(--cream);top:16px}.middle .speaker-name{color:var(--white);top:28px}
.headshot{position:absolute;right:0;bottom:0;width:62px;height:112px;background:linear-gradient(180deg,var(--photo-a),var(--photo-b));border-radius:26px 26px 0 0}
.forest-strip{left:0;bottom:0;width:545px;height:112px;background:linear-gradient(180deg,rgba(79,122,94,0),#2f5a45 55%,#3f6d4f)}
</style>
</head>
<body>
<div class="canvas">

  <!-- Poster -->
  <section class="piece poster">
    <div class="abs panel" style="left:349px;top:32px;width:180px;height:370px" role="img" aria-label="Illustrated pine tree on green panel"></div>
    <div class="abs badge" style="left:431px;top:11px;width:96px;height:96px"><span class="badge-name" style="font-size:17px">KV Rootline</span></div>
    <p class="abs presents" style="left:31px;top:38px;font-size:24px">KV Rootline presents</p>
    <h1 class="abs title" style="left:20px;top:74px;font-size:98px">SUMMER</h1>
    <div class="abs camp-lockup" style="left:34px;top:160px;gap:16px">
      <span class="camp-word" style="font-size:74px">CAMP</span><span class="year" style="font-size:50px">2023</span>
    </div>
    <div class="abs scene" style="left:35px;top:244px;width:282px;height:160px" role="img" aria-label="Illustrated yellow camping tent beside a small pine"></div>
    <div class="abs sun" style="left:315px;top:285px;width:60px;height:60px"></div>
    <p class="abs cond" style="left:31px;top:418px;font-size:31px">At Tamsin Brook Retreat<br>Center, Deadwood, SD</p>

    <p class="abs cond" style="left:31px;top:510px;font-size:17px;color:var(--white)">Teen Camp</p>
    <div class="abs speaker-card teen" style="left:32px;top:533px;width:135px;height:124px">
      <span class="speaker-tag">Speaker</span><span class="speaker-name">Luka<br>Brevant</span>
      <div class="headshot" role="img" aria-label="Headshot of speaker Luka Brevant"></div>
    </div>
    <div class="abs cond date" style="left:32px;top:664px;font-size:21px">
      <svg width="18" height="17" viewBox="0 0 18 17"><rect x="1" y="3" width="16" height="13" fill="var(--coral)"/><rect x="4" y="0" width="2" height="4" fill="var(--coral)"/><rect x="12" y="0" width="2" height="4" fill="var(--coral)"/><g fill="var(--forest)"><rect x="3" y="7" width="3" height="2"/><rect x="7.5" y="7" width="3" height="2"/><rect x="12" y="7" width="3" height="2"/><rect x="3" y="11" width="3" height="2"/><rect x="7.5" y="11" width="3" height="2"/><rect x="12" y="11" width="3" height="2"/></g></svg>June 5 - 9</div>

    <p class="abs cond" style="left:202px;top:534px;font-size:17px;color:var(--white)">High School Camp</p>
    <div class="abs speaker-card high" style="left:204px;top:557px;width:135px;height:124px">
      <span class="speaker-tag">Speaker</span><span class="speaker-name">Timo<br>Wexley</span>
      <div class="headshot" role="img" aria-label="Headshot of speaker Timo Wexley"></div>
    </div>
    <div class="abs cond date" style="left:205px;top:689px;font-size:21px">
      <svg width="18" height="17" viewBox="0 0 18 17"><rect x="1" y="3" width="16" height="13" fill="var(--coral)"/><rect x="4" y="0" width="2" height="4" fill="var(--coral)"/><rect x="12" y="0" width="2" height="4" fill="var(--coral)"/><g fill="var(--forest)"><rect x="3" y="7" width="3" height="2"/><rect x="7.5" y="7" width="3" height="2"/><rect x="12" y="7" width="3" height="2"/><rect x="3" y="11" width="3" height="2"/><rect x="7.5" y="11" width="3" height="2"/><rect x="12" y="11" width="3" height="2"/></g></svg>June 19 - 23</div>

    <p class="abs cond" style="left:375px;top:515px;font-size:17px;color:var(--white)">Middle School Camp</p>
    <div class="abs speaker-card middle" style="left:378px;top:538px;width:135px;height:125px">
      <span class="speaker-tag">Speaker</span><span class="speaker-name">Colin<br>Marbury</span>
      <div class="headshot" role="img" aria-label="Headshot of speaker Colin Marbury"></div>
    </div>
    <div class="abs cond date" style="left:379px;top:667px;font-size:21px">
      <svg width="18" height="17" viewBox="0 0 18 17"><rect x="1" y="3" width="16" height="13" fill="var(--coral)"/><rect x="4" y="0" width="2" height="4" fill="var(--coral)"/><rect x="12" y="0" width="2" height="4" fill="var(--coral)"/><g fill="var(--forest)"><rect x="3" y="7" width="3" height="2"/><rect x="7.5" y="7" width="3" height="2"/><rect x="12" y="7" width="3" height="2"/><rect x="3" y="11" width="3" height="2"/><rect x="7.5" y="11" width="3" height="2"/><rect x="12" y="11" width="3" height="2"/></g></svg>June 26 - 30</div>

    <div class="abs forest-strip" role="img" aria-label="Illustrated pine forest campsite with tents along the bottom"></div>
    <p class="abs cond" style="left:51px;top:768px;font-size:27px">Register Now</p>
    <div class="abs cta" style="left:249px;top:759px;width:254px;height:50px;font-size:24px">RivoTrailWeek.com</div>
  </section>

  <!-- Social square -->
  <section class="piece social">
    <div class="abs panel" style="left:314px;top:39px;width:187px;height:364px" role="img" aria-label="Illustrated pine tree on green panel"></div>
    <div class="abs badge" style="left:371px;top:27px;width:73px;height:73px"><span class="badge-name" style="font-size:13px">KV Rootline</span></div>
    <p class="abs presents" style="left:43px;top:34px;font-size:20px">KV Rootline presents</p>
    <h2 class="abs title" style="left:34px;top:62px;font-size:82px">SUMMER</h2>
    <div class="abs camp-lockup" style="left:45px;top:134px;gap:13px">
      <span class="camp-word" style="font-size:62px">CAMP</span><span class="year" style="font-size:42px">2023</span>
    </div>
    <div class="abs sun" style="left:288px;top:243px;width:64px;height:64px"></div>
    <p class="abs cond" style="left:41px;top:212px;font-size:16px">Teen Camp</p>
    <div class="abs cond date" style="left:41px;top:234px;font-size:15px">
      <svg width="13" height="12" viewBox="0 0 18 17"><rect x="1" y="3" width="16" height="13" fill="var(--coral)"/><rect x="4" y="0" width="2" height="4" fill="var(--coral)"/><rect x="12" y="0" width="2" height="4" fill="var(--coral)"/><g fill="var(--forest)"><rect x="3" y="7" width="3" height="2"/><rect x="7.5" y="7" width="3" height="2"/><rect x="12" y="7" width="3" height="2"/><rect x="3" y="11" width="3" height="2"/><rect x="7.5" y="11" width="3" height="2"/><rect x="12" y="11" width="3" height="2"/></g></svg>June 5 - 9</div>
    <p class="abs cond" style="left:154px;top:212px;font-size:16px">High School Camp</p>
    <div class="abs cond date" style="left:154px;top:234px;font-size:15px">
      <svg width="13" height="12" viewBox="0 0 18 17"><rect x="1" y="3" width="16" height="13" fill="var(--coral)"/><rect x="4" y="0" width="2" height="4" fill="var(--coral)"/><rect x="12" y="0" width="2" height="4" fill="var(--coral)"/><g fill="var(--forest)"><rect x="3" y="7" width="3" height="2"/><rect x="7.5" y="7" width="3" height="2"/><rect x="12" y="7" width="3" height="2"/><rect x="3" y="11" width="3" height="2"/><rect x="7.5" y="11" width="3" height="2"/><rect x="12" y="11" width="3" height="2"/></g></svg>June 19 - 23</div>
    <p class="abs cond" style="left:41px;top:263px;font-size:16px">Middle School Camp</p>
    <div class="abs cond date" style="left:41px;top:285px;font-size:15px">
      <svg width="13" height="12" viewBox="0 0 18 17"><rect x="1" y="3" width="16" height="13" fill="var(--coral)"/><rect x="4" y="0" width="2" height="4" fill="var(--coral)"/><rect x="12" y="0" width="2" height="4" fill="var(--coral)"/><g fill="var(--forest)"><rect x="3" y="7" width="3" height="2"/><rect x="7.5" y="7" width="3" height="2"/><rect x="12" y="7" width="3" height="2"/><rect x="3" y="11" width="3" height="2"/><rect x="7.5" y="11" width="3" height="2"/><rect x="12" y="11" width="3" height="2"/></g></svg>June 26 - 30</div>
    <p class="abs cond" style="left:37px;top:315px;font-size:23px">At Tamsin Brook Retreat<br>Center, Deadwood, SD</p>
    <div class="abs scene" style="left:37px;top:382px;width:216px;height:121px" role="img" aria-label="Illustrated yellow camping tent beside a small pine"></div>
    <p class="abs cond" style="left:346px;top:432px;font-size:19px">Register Now</p>
    <div class="abs cta" style="left:277px;top:462px;width:216px;height:43px;font-size:19px">RivoTrailWeek.com</div>
  </section>

  <!-- 16x9 title slide -->
  <section class="piece slide">
    <div class="abs panel" style="left:380px;top:48px;width:116px;height:225px" role="img" aria-label="Illustrated pine tree on green panel"></div>
    <div class="abs badge" style="left:402px;top:14px;width:65px;height:65px"><span class="badge-name" style="font-size:12px">KV Rootline</span></div>
    <p class="abs presents" style="left:50px;top:38px;font-size:19px">KV Rootline presents</p>
    <h2 class="abs title" style="left:43px;top:66px;font-size:80px">SUMMER</h2>
    <div class="abs camp-lockup" style="left:53px;top:134px;gap:12px">
      <span class="camp-word" style="font-size:58px">CAMP</span><span class="year" style="font-size:40px">2023</span>
    </div>
    <div class="abs scene" style="left:206px;top:184px;width:161px;height:88px" role="img" aria-label="Illustrated yellow camping tent beside a small pine"></div>
    <div class="abs sun" style="left:56px;top:213px;width:49px;height:49px"></div>
  </section>

</div>
</body>
</html>
```